creation of business cards for Velanto Sàrl

Velanto S% 26 # 224; rl is a soci% 26 # 233; t% 26 # 233; consultancy that accompanies companies in the development of their business on the market% 26 # 233; Switzerland by providing strategic contacts or market information; and by providing administrative or logistical support. Our consulting skills focus on sectors% 26 # 224; high value added% 26 # 233; e, such as trade in food goods% 26 # 39amp; drinks, fashion% 26amp; lifestyle, products and services for% 26 # 233; s in high-tech industries (pharmaceutical, chemical, m% 26 # 233; pricy 26% 23 #; cision) or sustainable solutions (% 26 # 233; energies renewable, mat% 26 # 233; recyclable materials). As part of the launch of our activity% 26 # 233;, we need% 26 # 39;% 26 # 233; to establish business cards to d% 26 # 233; work our new customers (Swiss or international).

Target Market(s)

Companies wishing to develop their activity% 26 # 233; s in Switzerland or% 26 # 224; l% 26 # 39;% 26 # 233; abroad (mainly in Europe).

Contact Information for Business Card

Prénom NOM
Velanto Sàrl
Bureau de Marvoisin
Rue des Tilleuls 47, 2000 Neuchâtel
Tél. : 032 718 46 39
info@velanto-example.ch
www.velanto-example.ch

Font styles to use
Serif
Sans Serif

Colors

Designer to choose colors to be used in the design.

Requirements
Must have
• The logo The name of the company% 26 # 233; t% 26 # 233; (Velanto S% 26 # 224; rl) One field for the mailing address One field for the number% 26 # 233; ro de t% 26 # 233; l% 26 # 233; phone One field for the % 26 # 39; email address and website

```html
<!DOCTYPE html>
<html lang="fr">
<head>
<meta charset="utf-8">
<title>Velanto Sàrl – cartes de visite</title>
<link rel="stylesheet" href="https://fonts.googleapis.com/css2?family=Roboto:wght@300;400;700&display=swap">
<style>
  :root {
    --backdrop: #9c9c9c;
    --brand-deep: #00405a;
    --brand-mist: #a8bccb;
    --paper: #ffffff;
  }
  * { margin: 0; padding: 0; box-sizing: border-box; }
  html, body {
    width: 1200px; height: 900px; overflow: hidden;
    background: var(--backdrop);
    font-family: "Roboto", Arial, sans-serif;
  }
  .stage { position: relative; width: 1200px; height: 900px; }
  .card {
    position: absolute; top: 214px;
    width: 270px; height: 474px;
    border-radius: 22px; overflow: hidden;
  }
  .card--front { left: 288px; background: var(--brand-deep); }
  .card--back { left: 641px; background: var(--paper); color: var(--brand-deep); text-align: center; }

  .front-wordmark {
    position: absolute; left: 0; right: 0; top: 610px; top: 396px;
    text-align: center; color: var(--paper);
    font-weight: 300; font-size: 31px; letter-spacing: 4px;
  }

  .brand-line {
    position: absolute; left: 34px; top: 79px;
    display: flex; align-items: center; gap: 17px;
  }
  .brand-mark {
    width: 31px; height: 31px; border-radius: 7px;
    background: var(--brand-deep);
  }
  .brand-name {
    font-weight: 300; font-size: 25px; letter-spacing: 2.5px;
    color: var(--brand-deep);
  }

  .person {
    position: absolute; left: 0; right: 0; top: 240px;
  }
  .person-name { font-weight: 700; font-size: 19px; line-height: 24px; }
  .person-company { font-weight: 300; font-size: 13px; color: var(--brand-mist); line-height: 16px; }

  .divider {
    position: absolute; left: 58px; width: 155px; height: 1px;
    background: var(--brand-deep);
  }
  .divider--icons { top: 298px; }
  .divider--plain { top: 376px; }
  .icon-row {
    position: absolute; top: 289px; left: 0; right: 0;
    display: flex; justify-content: center; gap: 2px;
  }
  .icon-row svg { display: block; }

  .contact-list {
    position: absolute; left: 0; right: 0; top: 315px;
    list-style: none; font-weight: 300; font-size: 13px; line-height: 16px;
  }
  .contact-list .muted { color: var(--brand-mist); }

  .address {
    position: absolute; left: 0; right: 0; top: 386px;
    font-style: normal; font-weight: 300; font-size: 13px; line-height: 16px;
  }
</style>
</head>
<body>
<main class="stage">
  <section class="card card--front" aria-label="Recto">
    <p class="front-wordmark">VELANTO</p>
  </section>

  <section class="card card--back" aria-label="Verso">
    <div class="brand-line">
      <span class="brand-mark" aria-hidden="true"></span>
      <span class="brand-name">VELANTO</span>
    </div>

    <div class="person">
      <p class="person-name">Prénom NOM</p>
      <p class="person-company">Velanto Sàrl</p>
    </div>

    <span class="divider divider--icons"></span>
    <div class="icon-row" aria-hidden="true">
      <svg width="18" height="18" viewBox="0 0 18 18">
        <circle cx="9" cy="9" r="8.5" fill="#a8bccb"/>
        <path d="M4.5 8.5c0-2 9-2 9 0v1h-2.5v-1h-4v1H4.5z M6 10h6l1 3H5z" fill="#fff"/>
      </svg>
      <svg width="18" height="18" viewBox="0 0 18 18">
        <circle cx="9" cy="9" r="8.5" fill="#a8bccb"/>
        <rect x="4.5" y="5.8" width="9" height="6.4" fill="none" stroke="#fff" stroke-width="1"/>
        <path d="M4.5 5.8L9 9.5l4.5-3.7" fill="none" stroke="#fff" stroke-width="1"/>
      </svg>
      <svg width="18" height="18" viewBox="0 0 18 18">
        <circle cx="9" cy="9" r="8.5" fill="#a8bccb"/>
        <circle cx="9" cy="9" r="4.6" fill="none" stroke="#fff" stroke-width="1"/>
        <ellipse cx="9" cy="9" rx="2" ry="4.6" fill="none" stroke="#fff" stroke-width="0.8"/>
        <path d="M4.4 9h9.2" stroke="#fff" stroke-width="0.8"/>
      </svg>
    </div>

    <ul class="contact-list">
      <li>032 718 46 39</li>
      <li>info@velanto-example.ch</li>
      <li>www.<span class="muted">velanto-example</span>.ch</li>
    </ul>

    <span class="divider divider--plain"></span>

    <address class="address">
      Bureau de Marvoisin<br>
      Rue des Tilleuls 47, 2000 Neuchâtel
    </address>
  </section>
</main>
</body>
</html>
```